Vodka Bottle Label - Lune Vodka

I need a bottle label for a vodka I'd like to make called Lune Vodka.
I would like a label that looks elegant and fresh. I would like some mountains and colours to be red and white. Open to other colours being added but not too colourful. "Lune" means fresh, dawn in polish, i would like if mountains or something extra was added to the label too. I would like the Lune Vodka name not to be too small.
The vodka is made in australia and is 37%.

I would love to have a little bit of gold colour in the label!

I will provide the back label words when completing my decision.

i'd like to make it more simple and less european looking. More australian.

I saw a bottle like this and i did like the concept.

https://www.oakbarrelcellars.com.au/spirits/grey-vodka-range?srsltid=XqTz81mwkPLd04-hr-q7w93nfbzkgd_mR2yTpaMWxJeQ6vcbTnZsLpo

Target Market(s)

Vodka Drinkers

Industry/Entity Type

Alcohol

Colors
EB3D1F
EC4F4E
F09395
F8D3D4
FCEDEE

Requirements
Must have
• red and white colours incorporated, mountains or freshness on it.
Nice to have
• Fresh and clean look. Classy

```html
<!DOCTYPE html>
<html lang="en">
<head>
<meta charset="utf-8">
<title>Lune Vodka – Bottle Label</title>
<link rel="stylesheet" href="https://fonts.googleapis.com/css2?family=Bodoni+Moda:wght@400;700&family=Jost:wght@300;400&display=swap">
<style>
  :root {
    --label-green: #37423a;
    --dawn-red: #b15a52;
    --snow-white: #ffffff;
    --leaf-grey: #6f7a72;
  }
  html, body {
    margin: 0;
    padding: 0;
    width: 1200px;
    height: 603px;
    overflow: hidden;
    background: var(--label-green);
  }
  .label {
    position: relative;
    width: 1200px;
    height: 603px;
    background: var(--label-green);
    color: var(--snow-white);
  }
  .label__frame {
    position: absolute;
    inset: 0;
  }
  .label__text {
    position: absolute;
    left: 0;
    width: 1200px;
    margin: 0;
    text-align: center;
    line-height: 1;
  }
  .brand-name {
    top: 296px;
    font-family: "Bodoni Moda", serif;
    font-weight: 400;
    font-size: 84px;
    letter-spacing: 0.01em;
  }
  .brand-type {
    top: 381px;
    font-family: "Bodoni Moda", serif;
    font-weight: 400;
    font-size: 31px;
  }
  .tagline {
    top: 429px;
    font-family: "Jost", sans-serif;
    font-weight: 300;
    font-size: 11px;
    letter-spacing: 0.04em;
    line-height: 16px;
  }
  .strength {
    top: 464px;
    font-family: "Bodoni Moda", serif;
    font-weight: 700;
    font-size: 25px;
    color: var(--dawn-red);
  }
  .origin {
    top: 502px;
    font-family: "Jost", sans-serif;
    font-weight: 400;
    font-size: 8.5px;
    letter-spacing: 0.5em;
    padding-left: 0.5em;
  }
</style>
</head>
<body>
  <main class="label">
    <svg class="label__frame" width="1200" height="603" viewBox="0 0 1200 603">
      <defs>
        <linearGradient id="peak-glow" x1="0" y1="0" x2="0" y2="1">
          <stop offset="0" stop-color="#b15a52"/>
          <stop offset="0.55" stop-color="#d9b3ae"/>
          <stop offset="1" stop-color="#f4f1f0"/>
        </linearGradient>
        <clipPath id="inside-arch">
          <circle cx="600" cy="303.5" r="188"/>
        </clipPath>
      </defs>
      <g class="dawn-arch" fill="none" stroke="var(--dawn-red)" stroke-width="4.5">
        <path d="M388.5 342 V303.5 A211.5 211.5 0 0 1 811.5 303.5 V342"/>
        <path d="M402.5 342 V303.5 A197.5 197.5 0 0 1 797.5 303.5 V342"/>
      </g>
      <rect class="mountain-sunrise" x="424" y="126" width="352" height="168" fill="url(#peak-glow)" clip-path="url(#inside-arch)" role="img" aria-label="Snow-capped mountain range in white with a red sunburst rising behind the peaks"/>
      <rect class="laurel laurel--left" x="408" y="350" width="68" height="111" fill="var(--leaf-grey)" opacity="0.6" role="img" aria-label="Grey leafy sprig curving up the left side"/>
      <rect class="laurel laurel--right" x="724" y="350" width="68" height="111" fill="var(--leaf-grey)" opacity="0.6" role="img" aria-label="Grey leafy sprig curving up the right side"/>
      <g class="strength-rules" stroke="var(--snow-white)" stroke-width="1.2">
        <line x1="435" y1="470" x2="569" y2="470"/>
        <line x1="435" y1="473" x2="569" y2="473"/>
        <line x1="435" y1="484" x2="569" y2="484"/>
        <line x1="435" y1="487" x2="569" y2="487"/>
        <line x1="631" y1="470" x2="765" y2="470"/>
        <line x1="631" y1="473" x2="765" y2="473"/>
        <line x1="631" y1="484" x2="765" y2="484"/>
        <line x1="631" y1="487" x2="765" y2="487"/>
      </g>
    </svg>

    <h1 class="label__text brand-name">LUNE</h1>
    <p class="label__text brand-type">VODKA</p>
    <p class="label__text tagline">FRESHNESS IN EVERY DROP OF<br>LUNE VODKA</p>
    <p class="label__text strength">37%</p>
    <p class="label__text origin">MADE IN AUSTRALIA</p>
  </main>
</body>
</html>
```